Create a business promotion flyer to leave in customer mailboxes. We are a bulk petroleum supplier, servicing any industry that requires diesel. Base in griffith NSW, servicing griffith area and surrounds.

Business Name - Terra Petro
Fuel@terrapetro-example.com.au
Marco - 0400 000 001 mtorrisi@terrapetro-example.com.au
Liam - 0400 000 002 lharcourt@terrapetro-example.com.au
Peter - 0400 000 003 pwinslow@terrapetro-example.com.au
Office 02 5550 0100

Bulk Fuel deliveries.
Oils & lubricants
Local Family owned business

```html
<!DOCTYPE html>
<html lang="en">
<head>
<meta charset="utf-8">
<title>Terra Petro – Bulk Fuel Flyer</title>
<link rel="stylesheet" href="https://fonts.googleapis.com/css2?family=Barlow:ital,wght@0,400;0,500;1,600;1,700;1,800&family=Barlow+Condensed:ital,wght@0,500;1,600;1,700&display=swap">
<style>
  :root{
    --red:#d11a1f;
    --red-deep:#b5151a;
    --charcoal:#26282b;
    --charcoal-2:#34373b;
    --ink:#1c1c1e;
    --white:#ffffff;
    --paper:#f3f4f5;
    --sky:#8fb6e0;
    --sky-light:#dfe9f4;
    --ground:#b9b5ae;
  }
  *{margin:0;padding:0;box-sizing:border-box}
  html,body{width:1200px;height:1200px;overflow:hidden;background:var(--white)}
  .canvas{position:relative;width:1200px;height:1200px}
  .flyer{position:absolute;left:400px;top:300px;width:400px;height:600px;overflow:hidden;
    background:linear-gradient(180deg,#fafafa 0%,var(--paper) 60%,#e8e9ea 100%);
    font-family:"Barlow",sans-serif;color:var(--ink)}
  .abs{position:absolute}
  .art{position:absolute;left:0;top:0}
  .tagline-corner{left:299px;top:48px;font:italic 700 10px/12.8px "Barlow",sans-serif;color:var(--white);text-transform:uppercase}
  .tagline-corner .hl{color:var(--red)}
  .wordmark{left:22px;top:108px;font:500 46px/1 "Barlow",sans-serif;color:var(--red);letter-spacing:-0.5px}
  .headline{left:23px;top:152px;font:italic 700 11.5px/1 "Barlow",sans-serif;text-transform:uppercase;color:var(--ink)}
  .headline .hl{color:var(--red)}
  .intro{left:23px;top:176px;width:150px;font:400 8.8px/13.6px "Barlow",sans-serif;color:var(--ink)}
  .service{left:0;height:37px;width:150px}
  .service .icon{position:absolute;left:0;top:0;width:41px;height:37px;background:var(--red);display:flex;align-items:center;justify-content:center}
  .service .label{position:absolute;left:51px;top:6px;font:italic 700 11.5px/12.8px "Barlow",sans-serif;color:var(--white);text-transform:uppercase}
  .s1{top:236px}.s2{top:282px}.s3{top:327px}.s4{top:373px}
  .band{left:0;top:419px;width:400px;height:47px;background:var(--red);text-align:center;color:var(--white)}
  .band .claim{margin-top:9px;font:italic 700 14.5px/1 "Barlow",sans-serif;letter-spacing:.6px;text-transform:uppercase}
  .band .sub{margin-top:4px;font:italic 600 6.6px/1 "Barlow",sans-serif;letter-spacing:.3px;text-transform:uppercase}
  .contacts{left:0;top:466px;width:400px;height:89px;background:var(--charcoal)}
  .person{position:absolute;top:10px;width:120px;text-align:center}
  .person .name{font:italic 700 9.5px/1 "Barlow",sans-serif;color:var(--red);text-transform:uppercase}
  .person .phone{margin-top:3px;font:italic 600 15px/1 "Barlow Condensed",sans-serif;color:var(--white);font-size:16.5px}
  .p1{left:10px}.p2{left:133px}.p3{left:255px}
  .rule{position:absolute;width:1px;background:#6b6e72}
  .r1{left:134px;top:14px;height:26px}.r2{left:254px;top:14px;height:26px}.r3{left:190px;top:55px;height:24px}
  .email{position:absolute;left:46px;top:54px;display:flex;align-items:center;gap:5px;color:var(--white);font:500 9px/1 "Barlow Condensed",sans-serif}
  .place{position:absolute;left:206px;top:54px;display:flex;align-items:center;gap:7px;color:var(--white)}
  .place .town{font:500 10.5px/1 "Barlow Condensed",sans-serif}
  .place .area{margin-top:2px;font:500 8px/1 "Barlow Condensed",sans-serif}
  .disc{width:25px;height:25px;border-radius:50%;background:var(--red);display:flex;align-items:center;justify-content:center;flex:none}
  .footer{left:0;top:555px;width:400px;height:45px;background:linear-gradient(90deg,var(--red) 0%,var(--red) 65%,var(--red-deep) 100%);
    color:var(--white);text-align:center;font:italic 700 9.8px/45px "Barlow",sans-serif;letter-spacing:.3px;text-transform:uppercase}
</style>
</head>
<body>
<div class="canvas">
  <section class="flyer">
    <svg class="art" width="400" height="420" viewBox="0 0 400 420">
      <defs>
        <linearGradient id="sceneFill" x1="0" y1="0" x2="0" y2="1">
          <stop offset="0" stop-color="var(--sky)"/>
          <stop offset="0.45" stop-color="var(--sky-light)"/>
          <stop offset="0.7" stop-color="#e9eaec"/>
          <stop offset="1" stop-color="var(--ground)"/>
        </linearGradient>
      </defs>
      <polygon points="285,105 400,150 400,419 120,419 230,210" fill="url(#sceneFill)" role="img" aria-label="Photo: white tanker truck under a blue sky"/>
      <polygon points="300,0 400,0 400,152 262,100" fill="#dcdcde" opacity=".8"/>
      <polygon points="312,0 400,0 400,152 262,100" fill="var(--charcoal)"/>
    </svg>

    <p class="abs tagline-corner">Fuelling<br><span class="hl">Local industry.</span><br>Keeping Griffith<br><span class="hl">moving.</span></p>

    <h1 class="abs wordmark">Terra Petro</h1>
    <h2 class="abs headline">Your <span class="hl">local</span> bulk fuel specialists</h2>
    <p class="abs intro">Proudly based in Griffith, NSW – servicing Griffith and surrounding areas.</p>

    <div class="abs service s1">
      <svg width="150" height="37" class="art"><polygon points="41,0 142,0 128,37 41,37" fill="var(--charcoal)"/></svg>
      <div class="icon"><svg width="18" height="22" viewBox="0 0 18 22"><path d="M9 1C6 7 2 10 2 14a7 7 0 0 0 14 0C16 10 12 7 9 1Z" fill="none" stroke="#fff" stroke-width="1.6"/></svg></div>
      <div class="label">Bulk fuel<br>deliveries</div>
    </div>
    <div class="abs service s2">
      <svg width="150" height="37" class="art"><polygon points="41,0 133,0 119,37 41,37" fill="var(--charcoal)"/></svg>
      <div class="icon"><svg width="30" height="18" viewBox="0 0 30 18"><path d="M2 5h6l3 3h9l7-4-8 9H9V8" fill="none" stroke="#fff" stroke-width="1.5" stroke-linejoin="round"/><path d="M27 10q1 2 0 3" stroke="#fff" stroke-width="1.4" fill="none"/></svg></div>
      <div class="label">Oils &amp;<br>lubricants</div>
    </div>
    <div class="abs service s3">
      <svg width="150" height="37" class="art"><polygon points="41,0 134,0 120,37 41,37" fill="var(--charcoal)"/></svg>
      <div class="icon"><svg width="20" height="24" viewBox="0 0 20 24"><rect x="2" y="2" width="10" height="20" rx="1.5" fill="#fff"/><rect x="4" y="4" width="6" height="5" fill="var(--red)"/><path d="M12 8h3v10a2 2 0 0 0 3 0V7l-3-3" fill="none" stroke="#fff" stroke-width="1.5"/></svg></div>
      <div class="label">Petrol<br>deliveries</div>
    </div>
    <div class="abs service s4">
      <svg width="150" height="37" class="art"><polygon points="41,0 160,0 146,37 41,37" fill="var(--charcoal)"/></svg>
      <div class="icon"><svg width="28" height="20" viewBox="0 0 28 20"><circle cx="14" cy="5" r="4" fill="#fff"/><circle cx="5" cy="8" r="3" fill="#fff"/><circle cx="23" cy="8" r="3" fill="#fff"/><path d="M7 19a7 7 0 0 1 14 0Z" fill="#fff"/><path d="M0 19a5 5 0 0 1 8-4l-1 4Z" fill="#fff"/><path d="M28 19a5 5 0 0 0-8-4l1 4Z" fill="#fff"/></svg></div>
      <div class="label">Local family<br>owned business</div>
    </div>

    <div class="abs band">
      <p class="claim">Reliable fuel. Local service. Every time.</p>
      <p class="sub">Delivering quality products &amp; service you can count on.</p>
    </div>

    <div class="abs contacts">
      <div class="person p1"><p class="name">Marco</p><p class="phone">0400 000 001</p></div>
      <span class="rule r1"></span>
      <div class="person p2"><p class="name">Liam</p><p class="phone">0400 000 002</p></div>
      <span class="rule r2"></span>
      <div class="person p3"><p class="name">Peter</p><p class="phone">0400 000 003</p></div>
      <div class="email">
        <span class="disc"><svg width="13" height="10" viewBox="0 0 13 10"><rect x=".5" y=".5" width="12" height="9" rx="1" fill="#fff"/><path d="M1 1l5.5 4.5L12 1" fill="none" stroke="var(--red)" stroke-width="1.2"/></svg></span>
        <span>Fuel@terrapetro-example.com.au</span>
      </div>
      <span class="rule r3"></span>
      <div class="place">
        <span class="disc"><svg width="11" height="14" viewBox="0 0 11 14"><path d="M5.5 0A5 5 0 0 0 .5 5c0 4 5 9 5 9s5-5 5-9a5 5 0 0 0-5-5Z" fill="#fff"/><circle cx="5.5" cy="5" r="1.8" fill="var(--red)"/></svg></span>
        <div><p class="town">Griffith NSW</p><p class="area">Servicing Griffith &amp; Surrounds</p></div>
      </div>
    </div>

    <p class="abs footer">Your partner in powering local industry</p>
  </section>
</div>
</body>
</html>
```